Brindlewave Systems Retractable Banner

Need a design for a retractable banner (approx. 63 inches x 24 inches) Provide us with different raw file types including: ai, png. We may end up ordering a banner that is larger or smaller so please ensure the design provided can be scaled accordingly.
Key Features:
One of the two logos shown below must be displayed (your choice). We can provide other file formats for the logo if needed.
Words that have to be shown:
Your *Data Collection Problems* End Here
Our technology transforms any building into an *IoT Smart Building*
Our *Monitoring and Alerting* capabilities give you full insight and control of your devices and buildings
Please note the words within *(stars) must be accentuated in some way, please use your creative freedom.
A design that fits the look and feel of our brand, as seen in our website here: https://brindlewavesys.example/ is encouraged

```html
<!DOCTYPE html>
<html lang="en">
<head>
<meta charset="utf-8">
<title>Brindlewave Systems Retractable Banner</title>
<link rel="stylesheet" href="https://fonts.googleapis.com/css2?family=Arimo:ital,wght@0,700;1,700&display=swap">
<style>
  :root {
    --teal: #199cae;
    --mist: #c1d6dc;
    --paper: #ffffff;
    --ink: #2b2b2b;
    --brand-ink: #0b5560;
    --edge: #9a9a9a;
  }
  html, body {
    margin: 0;
    padding: 0;
    width: 1200px;
    height: 3147px;
    overflow: hidden;
    background: var(--paper);
  }
  .banner {
    display: block;
    width: 1200px;
    height: 3147px;
  }
  .banner-frame { fill: var(--paper); stroke: var(--edge); stroke-width: 1.5; }
  .band { fill: var(--teal); }
  .stripe { fill: var(--paper); }
  .facet { fill: var(--mist); }
  .brand-mark { fill: var(--teal); }
  .brand-name {
    font-family: "Arimo", Arial, sans-serif;
    font-weight: 700;
    font-style: normal;
    font-size: 66px;
    fill: var(--brand-ink);
  }
  .message {
    font-family: "Arimo", Arial, sans-serif;
    font-weight: 700;
    font-style: italic;
    fill: var(--ink);
  }
  .message .accent { fill: var(--teal); }
  .message-sm { font-size: 40px; }
  .message-md { font-size: 44px; }
  .message-lg { font-size: 50px; }
</style>
</head>
<body>
<svg class="banner" viewBox="0 0 982 2576" xmlns="http://www.w3.org/2000/svg" role="img" aria-label="Brindlewave Systems retractable banner">
  <rect class="banner-frame" x="0.75" y="0.75" width="980.5" height="2574.5"/>

  <!-- Header brand -->
  <g class="brand brand-top">
    <circle class="brand-mark" cx="140" cy="183" r="30"/>
    <text class="brand-name" x="190" y="206" textLength="680" lengthAdjust="spacingAndGlyphs">Brindlewave Systems</text>
  </g>

  <!-- Central band -->
  <g class="band-group">
    <rect class="band" x="0" y="357" width="982" height="1826"/>
    <polygon class="stripe" points="0,746 982,392 982,600 0,955"/>
    <polygon class="facet" points="0,955 428,801 975,868 490,1045"/>
    <polygon class="stripe" points="0,1222 975,868 982,1133 0,1488"/>
    <polygon class="facet" points="0,1488 500,1308 982,1400 408,1609"/>
    <polygon class="stripe" points="0,1757 982,1400 982,1790 0,2145"/>
  </g>

  <!-- Messages -->
  <g class="messages">
    <text class="message message-sm" x="105" y="790" transform="rotate(-20.4 105 790)">Your</text>
    <text class="message message-md" x="105" y="835" transform="rotate(-20.4 105 835)" textLength="832" lengthAdjust="spacingAndGlyphs"><tspan class="accent">DATA COLLECTION PROBLEMS</tspan> end Here</text>

    <text class="message message-md" x="105" y="1295" transform="rotate(-20.2 105 1295)" textLength="826" lengthAdjust="spacingAndGlyphs">Our Technology Transforms Any Building</text>
    <text class="message message-md" x="345" y="1252" transform="rotate(-20.1 345 1252)" textLength="573" lengthAdjust="spacingAndGlyphs">into an <tspan class="accent">IoT SMART BUILDING</tspan></text>

    <text class="message message-lg" x="120" y="1835" transform="rotate(-20.6 120 1835)" textLength="796" lengthAdjust="spacingAndGlyphs">Our <tspan class="accent">MONITORING AND ALERTING</tspan></text>
    <text class="message message-lg" x="405" y="1780" transform="rotate(-21.4 405 1780)" textLength="494" lengthAdjust="spacingAndGlyphs">Capabilities Give You</text>
    <text class="message message-lg" x="185" y="1915" transform="rotate(-20.6 185 1915)" textLength="726" lengthAdjust="spacingAndGlyphs">Full Insight and Control of Your</text>
    <text class="message message-lg" x="380" y="1895" transform="rotate(-20.4 380 1895)" textLength="517" lengthAdjust="spacingAndGlyphs">Devices and Buildings</text>
  </g>

  <!-- Footer brand -->
  <g class="brand brand-bottom">
    <circle class="brand-mark" cx="140" cy="2378" r="30"/>
    <text class="brand-name" x="190" y="2401" textLength="680" lengthAdjust="spacingAndGlyphs">Brindlewave Systems</text>
  </g>
</svg>
</body>
</html>
```